Finance cashflow waterfall graphic

Recreate "Cashflow Waterfall Example 1" - waterfall term used to explain the different accounts and priority that need to be paid as part of a apartment building / project. Create simple, business professional graphic for real estate report. Check the inspiration image but change to dorm building, no people - potentially combine the two images... Ideally editable so I can change the names of the accounts / colors / etc.

```html
<!DOCTYPE html>
<html lang="en">
<head>
<meta charset="utf-8">
<title>Finance Cashflow</title>
<link rel="stylesheet" href="https://fonts.googleapis.com/css2?family=Poppins:wght@400;500&display=swap">
<style>
  :root {
    --page-bg: #ffffff;
    --rule: #bdbdbd;
    --title: #8a8a8d;
    --flow: #1ba3e1;
    --flow-light: #8dd3f5;
    --flow-dark: #2a8fd6;
    --building: #f58a5a;
    --tap: #fde2ad;
    --drop: #8fd6e6;
    --box-text: #111111;
  }
  html, body {
    margin: 0;
    width: 1200px;
    height: 1200px;
    overflow: hidden;
    background: var(--page-bg);
  }
  .cashflow-sheet {
    position: absolute;
    left: 0;
    top: 67px;
    width: 1200px;
    height: 1066px;
  }
  .rule { stroke: var(--rule); stroke-width: 2.5; }
  .connector { stroke: var(--flow); stroke-width: 2; fill: none; }
  .step-box { fill: #fff; stroke: var(--flow); stroke-width: 2; }
  .step-label {
    font-family: 'Poppins', sans-serif;
    font-size: 15.5px;
    fill: var(--box-text);
    text-anchor: middle;
  }
  .headline {
    font-family: 'Poppins', sans-serif;
    font-weight: 500;
    font-size: 57px;
    fill: var(--title);
    text-anchor: end;
    letter-spacing: -1px;
  }
</style>
</head>
<body>
<svg class="cashflow-sheet" viewBox="0 0 1044 927" xmlns="http://www.w3.org/2000/svg">
  <defs>
    <linearGradient id="flowGradient" x1="0" x2="1" y1="0" y2="0">
      <stop offset="0" stop-color="var(--flow-light)"/>
      <stop offset="0.5" stop-color="var(--flow-dark)"/>
      <stop offset="1" stop-color="#3aa4e2"/>
    </linearGradient>
  </defs>

  <line class="rule" x1="60" y1="82" x2="986" y2="82"/>

  <rect class="building-art" x="58" y="112" width="173" height="317" fill="var(--building)" role="img" aria-label="Illustration of an orange dormitory building with windows and arched doors"/>
  <rect class="tap-art" x="228" y="157" width="258" height="212" fill="var(--tap)" role="img" aria-label="Illustration of a faucet pouring from the building"/>

  <text class="headline" x="980" y="359">FINANCE</text>
  <text class="headline" x="980" y="407">CASHFLOW</text>

  <line class="rule" x1="60" y1="436" x2="381" y2="436"/>
  <line class="rule" x1="516" y1="436" x2="986" y2="436"/>
  <rect class="cash-stream" x="60" y="443" width="926" height="79" rx="10" fill="url(#flowGradient)" role="img" aria-label="Blue stream of cash with dollar symbols"/>
  <rect class="drop-art" x="399" y="367" width="104" height="143" rx="52" fill="var(--drop)" role="img" aria-label="Water drop with a dollar sign falling from the faucet"/>
  <line class="rule" x1="60" y1="530" x2="96" y2="530"/>
  <line class="rule" x1="122" y1="530" x2="986" y2="530"/>

  <!-- waterfall connectors -->
  <circle cx="110" cy="530" r="5" fill="var(--flow)"/>
  <path class="connector" d="M110 530 V588"/>
  <path class="connector" d="M155 603 H188"/>
  <path class="connector" d="M290 603 H318"/>
  <path class="connector" d="M367 625 V655"/>
  <path class="connector" d="M443 686 H469"/>
  <path class="connector" d="M613 686 H640"/>
  <path class="connector" d="M706 713 V740"/>
  <path class="connector" d="M772 688 H852 V740"/>

  <g class="step">
    <rect class="step-box" x="65" y="588" width="90" height="31" rx="5"/>
    <text class="step-label" x="110" y="609">Revenue</text>
  </g>
  <g class="step">
    <rect class="step-box" x="188" y="581" width="102" height="44" rx="5"/>
    <text class="step-label" x="239" y="600">Operating</text>
    <text class="step-label" x="239" y="617">Expenses</text>
  </g>
  <g class="step">
    <rect class="step-box" x="318" y="581" width="99" height="44" rx="5"/>
    <text class="step-label" x="367" y="599">Debt</text>
    <text class="step-label" x="367" y="616">Payment</text>
  </g>
  <g class="step">
    <rect class="step-box" x="317" y="655" width="126" height="62" rx="5"/>
    <text class="step-label" x="380" y="676">Asset</text>
    <text class="step-label" x="380" y="693">Management</text>
    <text class="step-label" x="380" y="710">Fees</text>
  </g>
  <g class="step">
    <rect class="step-box" x="469" y="659" width="144" height="54" rx="5"/>
    <text class="step-label" x="541" y="684">Recapitalization</text>
    <text class="step-label" x="541" y="701">Accounts</text>
  </g>
  <g class="step">
    <rect class="step-box" x="640" y="659" width="132" height="54" rx="5"/>
    <text class="step-label" x="706" y="686">Incentive</text>
    <text class="step-label" x="706" y="703">Fees</text>
  </g>
  <g class="step">
    <rect class="step-box" x="596" y="740" width="176" height="72" rx="5"/>
    <text class="step-label" x="684" y="761">Sustainment</text>
    <text class="step-label" x="684" y="778">Reserves / Member</text>
    <text class="step-label" x="684" y="795">Distribution (60%)</text>
  </g>
  <g class="step">
    <rect class="step-box" x="810" y="740" width="176" height="72" rx="5"/>
    <text class="step-label" x="898" y="765">Private Returns /</text>
    <text class="step-label" x="898" y="782">Managing Member</text>
    <text class="step-label" x="898" y="799">Distribution (40%)</text>
  </g>

  <line class="rule" x1="60" y1="844" x2="986" y2="844"/>
</svg>
</body>
</html>
```